Brightwell Harbor Property Maintenance and Construction Company require new business card design

We are a property maintenance and construction company that offer a total range of property maintenance construction services and have been too busy dealing with the running of the office and completing jobs to update our business cards. We have recently had a new logo designed for us and are needing to update our cards (and we also have new staff requiring business cards. We would ideally want to stay with the orange, black and grey theme. I have attached current business cards and also our new logo. Looking forward to feedback and ideas.

Target Market(s)

Real estate agents, local governments, companies, residential

Industry/Entity Type

Property Maintenance

Contact Information for Business Card

File uploaded has names and phone numbers for staff. We also need to add a card for a new staff member, which can be provided.

Colors
f37022

Requirements
Must have
• Must have logos for Certified Fabrication Steward and Prime Erector for which we are members of. Also a description of what services we provide
Should not have
• any "flowery" fonts and design. We are a construction company, so probably something very standard...but also not just a regular font (ie Arial!)

```html
<!DOCTYPE html>
<html lang="en">
<head>
<meta charset="utf-8">
<title>Brightwell Harbor – Business Cards</title>
<link rel="stylesheet" href="https://fonts.googleapis.com/css2?family=Arimo:wght@400;700&display=swap">
<style>
  :root{
    --orange:#f37022;
    --orange-light:#f7a24a;
    --orange-deep:#e0601a;
    --grey:#8a8b8d;
    --grey-dark:#5d5e60;
    --ink:#3a3a3c;
    --paper:#ffffff;
    --paper-shade:#eeeeee;
    --stage:#e9e6e2;
  }
  *{box-sizing:border-box;margin:0;padding:0}
  html,body{width:1200px;height:1023px;overflow:hidden}
  body{background:var(--stage);font-family:"Arimo",Arial,sans-serif;position:relative}
  .card{position:absolute;top:360px;width:525px;height:300px;overflow:hidden;box-shadow:0 6px 18px rgba(0,0,0,.18)}

  /* front */
  .card-front{left:45px;background:linear-gradient(180deg,var(--paper),var(--paper-shade))}
  .brand{position:absolute;left:36px;top:34px;display:flex;align-items:center;gap:10px}
  .brand-mark{width:22px;height:22px;background:var(--orange)}
  .brand-name{font-size:30px;font-weight:700;color:var(--orange);letter-spacing:-.5px}
  .brand-sub{position:absolute;left:36px;top:76px;font-size:12px;letter-spacing:4px;color:var(--grey)}
  .name-band{position:absolute;left:0;right:0;top:112px;height:36px;background:linear-gradient(90deg,var(--orange-deep),var(--orange) 50%,var(--orange-light));display:flex;align-items:center;padding-left:150px;color:#fff;font-size:17px}
  .name-band strong{font-weight:700}
  .name-band .role{font-size:13px;margin-left:8px;padding-left:8px;border-left:1.5px solid #fff}
  .band-rule{position:absolute;left:0;right:0;height:2px;background:var(--grey)}
  .contacts{position:absolute;left:36px;top:176px;list-style:none;font-size:13px;color:var(--ink);line-height:21px}
  .contacts li{display:flex;align-items:center;gap:8px}
  .contacts svg{width:12px;height:12px}
  .licence{position:absolute;right:30px;top:160px;font-size:12px;color:var(--ink);text-align:right}
  .memberships{position:absolute;right:30px;top:186px;display:flex;flex-direction:column;align-items:flex-end;gap:10px;font-size:10px;color:var(--ink)}
  .membership{display:flex;align-items:center;gap:7px}
  .badge-round{width:26px;height:26px;border-radius:50%;background:#d8d8d8;border:2px solid var(--grey)}
  .badge-square{width:26px;height:26px;background:#2a3a6e}

  /* back */
  .card-back{left:630px;background:linear-gradient(120deg,var(--orange-deep),var(--orange) 45%,var(--orange-light))}
  .back-header{position:absolute;left:0;right:0;top:0;height:40px;background:var(--grey);color:#fff;font-weight:700;font-size:17px;display:flex;align-items:center;padding-left:22px}
  .service-list{position:absolute;top:52px;color:#fff;font-size:13px;line-height:17px;list-style:none}
  .service-list.core{left:22px}
  .service-list.core li::before{content:"• "}
  .service-list.trades{right:22px;text-align:right}
  .back-brand{position:absolute;left:22px;top:204px}
  .back-brand .brand-name{color:var(--ink);font-size:22px}
  .back-brand .brand-sub{position:static;display:block;font-size:9px;letter-spacing:3px;color:var(--grey-dark);margin-top:2px}
  .back-footer{position:absolute;left:0;right:0;bottom:8px;height:28px;background:var(--grey);color:#fff;font-size:12px;display:flex;align-items:center;justify-content:flex-end;padding-right:22px}
  .back-edge{position:absolute;left:0;right:0;bottom:0;height:8px;background:var(--orange-deep)}
</style>
</head>
<body>

<section class="card card-front" aria-label="Business card front">
  <div class="brand">
    <span class="brand-mark"></span>
    <span class="brand-name">Brightwell Harbor</span>
  </div>
  <div class="brand-sub">PROPERTY SERVICES</div>

  <div class="band-rule" style="top:106px"></div>
  <div class="name-band"><strong>Dana Merriot</strong><span class="role">Director</span></div>
  <div class="band-rule" style="top:154px"></div>

  <ul class="contacts">
    <li><svg viewBox="0 0 12 12"><rect width="12" height="12" rx="2" fill="#f37022"/><rect x="4" y="2" width="4" height="8" rx="1" fill="#fff"/></svg>0400 555 812</li>
    <li><svg viewBox="0 0 12 12"><rect width="12" height="12" rx="2" fill="#f37022"/><path d="M3 3l2 0 1 2-1 1a5 5 0 0 0 2 2l1-1 2 1 0 2a7 7 0 0 1-7-7z" fill="#fff"/></svg>1300 555 019</li>
    <li><svg viewBox="0 0 12 12"><rect width="12" height="12" rx="2" fill="#f37022"/><rect x="2.5" y="3.5" width="7" height="5" fill="none" stroke="#fff"/><path d="M2.5 3.5l3.5 3 3.5-3" fill="none" stroke="#fff"/></svg>dana@brightwellharbor.example</li>
    <li><svg viewBox="0 0 12 12"><rect width="12" height="12" rx="2" fill="#f37022"/><circle cx="6" cy="6" r="3.5" fill="none" stroke="#fff"/><path d="M2.5 6h7M6 2.5v7" stroke="#fff"/></svg>www.brightwellharbor.example</li>
  </ul>

  <p class="licence">Licence No. CB-L 40728</p>
  <div class="memberships">
    <div class="membership"><span>Certified Fabrication Steward</span><span class="badge-round"></span></div>
    <div class="membership"><span>Prime Erector</span><span class="badge-square"></span></div>
  </div>
</section>

<section class="card card-back" aria-label="Business card back">
  <header class="back-header">Offering All Property Maintenance Services</header>
  <ul class="service-list core">
    <li>Programmed Maintenance</li>
    <li>Essential Services</li>
    <li>Maintenance Planning</li>
    <li>Reactionary Maintenance</li>
    <li>Commercial/Residential</li>
    <li>Body Corporate</li>
    <li>Insurance Claims</li>
    <li>24 Hour On Call</li>
  </ul>
  <ul class="service-list trades">
    <li>Carpentry</li>
    <li>Plumbing</li>
    <li>Electrical</li>
    <li>Painting</li>
    <li>Tiling</li>
    <li>Plastering</li>
    <li>Garden Maintenance</li>
    <li>Cleaning Services</li>
    <li>Waterproofing</li>
    <li>All Handyman Services</li>
  </ul>
  <div class="back-brand">
    <span class="brand-name">Brightwell Harbor</span>
    <span class="brand-sub">PROPERTY SERVICES</span>
  </div>
  <footer class="back-footer">42 Ledger Court Clayford Vic 3190</footer>
  <div class="back-edge"></div>
</section>

</body>
</html>
```